bramblecrest paving card makeover

were a excavation/paving contractor from Monterey ca, I'm looking to have a card designed front and back that has company details on the front and a list of the services we offer on the back.

Target Market(s)

home owners property management companies

Industry/Entity Type

Contractor

Contact Information for Business Card

bramblecrest paving 418 larkmoor st Monterey ca. licensed, insured and bonded
lic#657920 gerald pinsky operations manager

Font styles to use
Serif
Sans Serif

Colors
f78f20

Requirements
Must have
• a list of my services on back, asphalt construction and maintenance, drainage, foundations, retaining walls, chip seals, excavation, grading, landscape ground work, interlocking paver, hydro-seeding, structured and driveway demolition, utility trenching and stump removal.
Nice to have
• my new domain and page address I'm acquiring from pixel bazaar.

```html
<!DOCTYPE html>
<html lang="en">
<head>
<meta charset="utf-8">
<title>Bramblecrest Paving – Business Card</title>
<link href="https://fonts.googleapis.com/css2?family=Oswald:wght@600&family=Roboto:wght@400;500&family=Work+Sans:wght@400;500&display=swap" rel="stylesheet">
<style>
  :root {
    --backdrop: #3a312d;
    --card: #1b1b1b;
    --card-edge: #f78f20;
    --accent: #f78f20;
    --ink: #f2f2f2;
    --ink-soft: #d9d9d9;
  }
  * { box-sizing: border-box; margin: 0; padding: 0; }
  html, body { width: 1200px; height: 715px; overflow: hidden; }
  body {
    background: var(--backdrop);
    font-family: "Work Sans", Arial, sans-serif;
    position: relative;
  }
  .card {
    position: absolute;
    top: 215px;
    width: 500px;
    height: 286px;
    background: var(--card);
    border-radius: 6px;
    color: var(--ink);
    box-shadow: 0 10px 26px rgba(0,0,0,.45);
  }
  .card--back { left: 60px; border-bottom: 5px solid var(--card-edge); }
  .card--front { left: 640px; }

  .brand {
    display: flex;
    align-items: center;
    gap: 8px;
    font-family: "Work Sans", Arial, sans-serif;
    font-weight: 500;
    color: var(--ink);
    text-transform: uppercase;
    letter-spacing: .06em;
  }
  .brand__dot {
    width: 12px; height: 12px;
    border-radius: 50%;
    background: var(--ink);
    flex: none;
  }

  /* back */
  .card--back .brand {
    position: absolute;
    top: 42px; left: 0; right: 0;
    justify-content: center;
    font-size: 15px;
  }
  .services {
    position: absolute;
    top: 104px; left: 30px; right: 30px;
    text-align: center;
  }
  .services__title {
    font-family: "Roboto", Arial, sans-serif;
    font-weight: 500;
    color: var(--accent);
    font-size: 15px;
    letter-spacing: .02em;
    margin-bottom: 8px;
  }
  .services__list {
    font-family: "Roboto", Arial, sans-serif;
    font-size: 12.5px;
    line-height: 1.55;
    color: var(--ink);
  }

  /* front */
  .card--front .brand {
    position: absolute;
    top: 128px; left: 30px;
    width: 200px;
    font-size: 14px;
    line-height: 1.3;
  }
  .divider {
    position: absolute;
    left: 248px; top: 50px;
    width: 2px; height: 186px;
    background: var(--accent);
  }
  .details {
    position: absolute;
    left: 270px; top: 48px; right: 20px;
    font-size: 12.5px;
    line-height: 1.45;
    color: var(--ink-soft);
  }
  .details__name {
    font-family: "Oswald", Arial, sans-serif;
    font-weight: 600;
    font-size: 24px;
    color: var(--accent);
    text-transform: uppercase;
    letter-spacing: .02em;
    line-height: 1.1;
    margin-bottom: 4px;
  }
  .details__block { margin-bottom: 12px; }
  .contact { list-style: none; }
  .contact li { display: flex; align-items: center; gap: 9px; }
  .contact svg { width: 12px; height: 12px; flex: none; fill: var(--accent); }
  .highlight { color: var(--accent); }
</style>
</head>
<body>

<section class="card card--back" aria-label="Card back: services">
  <div class="brand"><span class="brand__dot"></span>Bramblecrest Paving</div>
  <div class="services">
    <h2 class="services__title">SERVICES</h2>
    <p class="services__list">
      asphalt construction and maintenance | drainage | foundations | retaining walls,
      chip seals | excavation | grading | landscape ground work | interlocking paver,
      hydro-seeding | structured and driveway demolition,
      utility trenching and stump removal.
    </p>
  </div>
</section>

<section class="card card--front" aria-label="Card front: contact details">
  <div class="brand"><span class="brand__dot"></span>Bramblecrest Paving</div>
  <div class="divider"></div>
  <div class="details">
    <div class="details__block">
      <h1 class="details__name">Dorian Vale</h1>
      <div>Managing Director</div>
      <div>Lic# 657920</div>
    </div>
    <div class="details__block">
      <div>418 Larkmoor St,</div>
      <div>Monterey, CA</div>
    </div>
    <ul class="contact">
      <li>
        <svg viewBox="0 0 24 24" aria-hidden="true"><path d="M6.6 10.8a15.1 15.1 0 0 0 6.6 6.6l2.2-2.2c.3-.3.7-.4 1-.2 1.1.4 2.3.6 3.6.6.6 0 1 .4 1 1V20c0 .6-.4 1-1 1A17 17 0 0 1 3 4c0-.6.4-1 1-1h3.5c.6 0 1 .4 1 1 0 1.3.2 2.5.6 3.6.1.3 0 .7-.2 1z"/></svg>
        +1 831 555 0147
      </li>
      <li>
        <svg viewBox="0 0 24 24" aria-hidden="true"><path d="M2 5h20v14H2z M2 5l10 8 10-8" stroke="#1b1b1b" stroke-width="1.5"/></svg>
        info@bramblecrest.com
      </li>
      <li>
        <svg viewBox="0 0 24 24" aria-hidden="true"><circle cx="12" cy="12" r="10"/><path d="M2 12h20M12 2c3 3 3 17 0 20M12 2c-3 3-3 17 0 20" stroke="#1b1b1b" stroke-width="1.5" fill="none"/></svg>
        <span>www.<span class="highlight">bramblecrest</span>.com</span>
      </li>
    </ul>
  </div>
</section>

</body>
</html>
```